Anzeigengestaltung für Apotheke
Zielgruppe
Lindmoor-Apotheke
klassische Vor Ort Apotheke, Zielgruppe ältere Menschen und Gesundheitsbewusste Menschen, die ihren Cholesterinwert wissen wollen.
Aufgabenstellung
Keine Speziellen, außer, dass unser Logo in die Anzeige integriert werden soll. Anzeige in DIN A 6 Format und sollte folgenden Inhalt haben:
Irgend ein Teaser : (Gern auch mal im Internet gucken bei anderen Apotheken)
Cholesterin- Woche vom 24.-29. Oktober
Wir messen Ihren Cholesterol Wert inklusive HDL, LDL und Gesamtcholesterin
Anmeldung erbeten bei Frau Hesse: hesse@lindmoor-apotheke.example oder unter 0761 58 72 19

```html
<!DOCTYPE html>
<html lang="de">
<head>
<meta charset="utf-8">
<title>Lindmoor-Apotheke – Cholesterin-Woche</title>
<link rel="stylesheet" href="https://fonts.googleapis.com/css2?family=Open+Sans:wght@400;600;700;800&family=Nothing+You+Could+Do&display=swap">
<style>
  :root {
    --green: #1f5e2e;
    --green-dark: #184d25;
    --orange: #c9521f;
    --orange-dark: #8f3510;
    --paper: #f4f4f2;
    --backdrop: #e4e5e3;
    --white: #ffffff;
    --red: #c8141c;
  }
  * { margin: 0; padding: 0; box-sizing: border-box; }
  html, body { width: 1200px; height: 800px; overflow: hidden; }
  body {
    background: var(--backdrop);
    font-family: "Open Sans", Arial, sans-serif;
    display: flex; align-items: center; justify-content: center;
  }
  .flyer {
    position: relative;
    width: 1100px; height: 778px;
    background: var(--paper);
    overflow: hidden;
    box-shadow: 0 6px 24px rgba(0,0,0,.18);
  }
  .brand {
    position: absolute; left: 40px; top: 34px; z-index: 2;
    display: flex; align-items: center; gap: 14px;
  }
  .brand-dot { width: 62px; height: 62px; border-radius: 50%; background: var(--green); }
  .brand-name { color: var(--green); font-weight: 800; font-size: 36px; letter-spacing: .5px; }
  .tagline {
    position: absolute; left: 300px; top: 112px; z-index: 2;
    font-family: "Nothing You Could Do", cursive;
    color: var(--red); font-size: 30px; line-height: 1.2; text-align: right;
  }
  .photo {
    position: absolute; left: 0; top: 150px; width: 630px; height: 440px; z-index: 1;
    background:
      linear-gradient(180deg, var(--paper) 0%, rgba(244,244,242,0) 22%),
      linear-gradient(135deg, #f7f7f6 0%, #e6e8e8 45%, #d3d6d8 70%, #b9c9b2 100%);
  }
  .labels { position: absolute; left: 20px; top: 500px; z-index: 2; }
  .label {
    display: inline-block; background: var(--green); color: var(--white);
    font-weight: 700; padding: 2px 16px; margin-bottom: 6px;
  }
  .label--name { font-size: 24px; }
  .label--owner { font-size: 22px; display: block; width: fit-content; }
  .contact {
    position: absolute; left: 36px; top: 612px;
    color: var(--green); font-size: 20px; line-height: 1.45; font-style: normal;
  }
  .contact b { font-weight: 800; }
  .panel {
    position: absolute; right: 0; top: 0; width: 470px; height: 100%;
    background: var(--green); color: var(--white); text-align: center;
  }
  .title {
    margin-top: 70px; font-weight: 800; font-size: 44px; line-height: 1.12; letter-spacing: 1px;
  }
  .ribbon { position: relative; margin: 20px auto 0; width: 440px; height: 150px; }
  .ribbon svg { position: absolute; inset: 0; }
  .ribbon-text {
    position: absolute; inset: 0; display: flex; flex-direction: column; justify-content: center;
    font-weight: 800; font-size: 38px; line-height: 1.1; letter-spacing: 1px;
  }
  .offer { margin: 30px 30px 0; font-size: 25px; line-height: 1.3; font-weight: 600; }
  .signup { margin: 30px 10px 0; font-size: 25px; line-height: 1.3; font-weight: 600; }
  .signup b { font-weight: 800; }
  .signup .signup-mail { font-size: 22px; white-space: nowrap; }
  .signup .nowrap { white-space: nowrap; }
</style>
</head>
<body>
  <main class="flyer">
    <div class="brand">
      <span class="brand-name">Lindmoor</span>
      <span class="brand-dot"></span>
      <span class="brand-name">Apotheke</span>
    </div>
    <p class="tagline">Gesundheit mitten<br>in Kirchwald!</p>

    <div class="photo" role="img" aria-label="Foto: Apothekerin misst mit Stechhilfe und Messgerät den Cholesterinwert am Finger einer Kundin"></div>

    <div class="labels">
      <span class="label label--name">Lindmoor-Apotheke</span>
      <span class="label label--owner">Apothekerin Dr. Marlene Voss-Albrecht</span>
    </div>
    <address class="contact">
      Lindenweg 12 79199 Kirchwald &nbsp;|&nbsp; <b>T :</b> (0761) 58 72 19<br>
      <b>F :</b> (0761) 58 72 20 &nbsp;|&nbsp; info@lindmoor-apotheke.example<br>
      www.lindmoor-apotheke.example
    </address>

    <section class="panel">
      <h1 class="title">CHOLESTERIN-<br>WOCHE</h1>
      <div class="ribbon">
        <svg viewBox="0 0 440 150" aria-hidden="true">
          <polygon points="40,130 0,130 20,108" fill="var(--orange-dark)"/>
          <polygon points="400,130 440,130 420,108" fill="var(--orange-dark)"/>
          <polygon points="30,10 410,10 440,120 420,140 20,140 0,120" fill="var(--orange)"/>
        </svg>
        <div class="ribbon-text"><span>VOM 24.-29.</span><span>OKTOBER</span></div>
      </div>
      <p class="offer">Wir messen Ihren Cholesterol Wert inklusive HDL, LDL und Gesamtcholesterin</p>
      <p class="signup">Anmeldung erbeten bei<br><b>Frau Hesse:</b><br><b class="signup-mail">hesse@lindmoor-apotheke.example</b><br>oder unter <b class="nowrap">0761 58 72 19</b></p>
    </section>
  </main>
</body>
</html>
```